Wedding Vows Poster for a Frame (anniversary gift )

I need an 8 X11 copy of both or wedding vows that I can frame in a classy and timeless modern font to frame for our house .

see file attach for text (vows)

project is now close thank you for all your help

```html
<!DOCTYPE html>
<html lang="en">
<head>
<meta charset="utf-8">
<title>Wedding Vows Poster</title>
<link rel="stylesheet" href="https://fonts.googleapis.com/css2?family=Italianno&family=Kaushan+Script&family=Pathway+Gothic+One&family=Cinzel&family=Great+Vibes&family=UnifrakturMaguntia&family=Alegreya+Sans&family=Pirata+One&display=swap">
<style>
  :root {
    --backdrop: #1c1c1c;
    --paper: #ffffff;
    --ink: #0a0a0a;
    --heart-deep: #c970b0;
    --heart-soft: #e9b9da;
    --silver-dark: #9a9ca1;
    --silver-light: #e6e8ea;
  }
  * { margin: 0; padding: 0; box-sizing: border-box; }
  html, body { width: 1200px; height: 1200px; overflow: hidden; background: var(--backdrop); }
  .canvas { position: relative; width: 1200px; height: 1200px; }
  .poster {
    position: absolute; left: 215px; top: 75px; width: 795px; height: 1093px;
    background: var(--paper); color: var(--ink); overflow: hidden;
  }
  .line { position: absolute; white-space: nowrap; line-height: 1; }
  .script-thin { font-family: "Italianno", cursive; }
  .script-bold { font-family: "Kaushan Script", cursive; }
  .condensed { font-family: "Pathway Gothic One", sans-serif; }
  .caps-serif { font-family: "Cinzel", serif; letter-spacing: 0.5px; }
  .blackletter { font-family: "UnifrakturMaguntia", serif; }
  .humanist { font-family: "Alegreya Sans", sans-serif; }
  .heart-art {
    position: absolute; left: 55px; top: 320px; width: 670px; height: 390px;
    background: radial-gradient(ellipse at 50% 45%, var(--heart-deep) 0%, var(--heart-deep) 45%, var(--heart-soft) 75%, rgba(255,255,255,0) 100%);
  }
  .love-title { font-family: "Great Vibes", cursive; font-size: 160px; left: 130px; top: 345px; }
  .love-you { font-family: "Great Vibes", cursive; font-size: 40px; left: 290px; top: 500px; }
  .love-name { font-family: "Pirata One", cursive; font-size: 96px; left: 300px; top: 535px; letter-spacing: 2px; }
  .rings-art {
    position: absolute; left: 605px; top: 865px; width: 165px; height: 205px;
    background: linear-gradient(90deg, var(--silver-dark), var(--silver-light) 50%, var(--silver-dark));
    border-radius: 40px;
  }
</style>
</head>
<body>
<div class="canvas">
  <article class="poster">
    <p class="line script-thin" style="left:30px;top:28px;font-size:55px;">Three years ago I fell in love with you</p>
    <p class="line script-bold" style="left:235px;top:78px;font-size:36px;">on our journey trough Peru,</p>
    <p class="line condensed" style="left:50px;top:118px;font-size:46px;">your love for life , your drive, your beautiful smile,</p>
    <p class="line script-thin" style="left:168px;top:162px;font-size:39px;">and natural beauty were at the time what got my attention.</p>
    <p class="line script-bold" style="left:43px;top:196px;font-size:36px;">Now that I know much more about you</p>
    <p class="line script-thin" style="left:175px;top:234px;font-size:35px;">I have realize how much more complete of an individual you are.</p>
    <p class="line caps-serif" style="left:105px;top:270px;font-size:23px;">FOR A LONG TIME I WISH I HAD MEET YOU BEFORE</p>
    <p class="line caps-serif" style="left:88px;top:300px;font-size:23px;">HOWEVER ONLY NOW I CAN APPRECIATE YOU FULLY.</p>

    <div class="heart-art" role="img" aria-label="Painted pink brush heart illustration"></div>

    <p class="line love-title">I Love</p>
    <p class="line love-you">you</p>
    <p class="line love-name">MARINA</p>

    <p class="line script-bold" style="left:95px;top:652px;font-size:34px;">This ring represents my commitment to you as</p>
    <p class="line script-bold" style="left:240px;top:688px;font-size:34px;">your partner and to our marriage.</p>
    <p class="line blackletter" style="left:185px;top:730px;font-size:22px;">As your partner I am committed to a life where</p>
    <p class="line blackletter" style="left:133px;top:764px;font-size:22px;">we can have it all.&nbsp; By all I mean an amazing relationship</p>
    <p class="line blackletter" style="left:208px;top:796px;font-size:22px;">where we can share a fulfilling life together.</p>

    <p class="line humanist" style="left:22px;top:832px;font-size:34px;">As your husband I promise to be loyal and</p>
    <p class="line humanist" style="left:127px;top:867px;font-size:34px;">give you the best that I can,</p>
    <p class="line humanist" style="left:86px;top:911px;font-size:17px;">protect and cherish you I will always be there for you trough</p>
    <p class="line humanist" style="left:195px;top:931px;font-size:28px;">good and hard time.</p>

    <p class="line script-thin" style="left:55px;top:985px;font-size:46px;">I will grow old with</p>
    <p class="line script-thin" style="left:105px;top:1020px;font-size:46px;">you and love you forever.</p>
    <p class="line script-bold" style="left:430px;top:1030px;font-size:44px;">- Daniel</p>

    <div class="rings-art" role="img" aria-label="Photo of two silver wedding rings tied with a red bow"></div>
  </article>
</div>
</body>
</html>
```